Business card and stationery design

Harbor & Summit Gatherings is a leading event and conference design and management company.
Please view harborandsummit.com.au

The business cards needs to convey:
- professionalism and competency
- exclusivity
- memorable experiences and quality

The business card needs to have the following aspects:
- double sided
- Full colour CMYK
- Printed on either high gloss matt card (designer to recommend)

For the business stationery we require:
- Letterhead with top banner and bottom footer
- A thank you card design
- a with compliments slip design
- a MS slidemaker and MS pagesetter client presentation slide design which includes cover page and then a standard presentation page
(Note- we do NOT require an envelope design- who sends letters these days!)

The company image is using the key colours of gold, silver and black.
A black background to the business card has been used before and is preferred although we are open to options.

Target Market(s)

High end corporations and businesses that require their events and conferences to be exceptionally well designed and managed

Industry/Entity Type

Business

Contact Information for Business Card

FRONT:

Darcy Whitlow
- Event and Conference Specialist

Mobile- +61 (0) 491 338 027
Office- 1300 862 419
darcyw@harborandsummit.com.au

Web- harborandsummit.com.au

BACK:

- Event and

Font styles to use
Other font styles liked:
• The logo designer used Trajan Pro Bold 3 for the font text in the logo

Requirements
Must have
• Amazing design of the following:
• - business card (double sided)
• - letterhead
• - client thank you card
• - slidemaker and pagesetter client presentation design files

```html
<!DOCTYPE html>
<html lang="en">
<head>
<meta charset="utf-8">
<title>Harbor &amp; Summit Gatherings – Business Card</title>
<link href="https://fonts.googleapis.com/css2?family=Cinzel:wght@600&family=Open+Sans:wght@400;700&display=swap" rel="stylesheet">
<style>
  :root {
    --backdrop: #3a322d;
    --card-black: #0c0c0c;
    --gold: #d9ad2e;
    --silver: #c9c9c9;
    --white: #f2f2f2;
    --rule-gold: #8a6d1f;
  }
  * { margin: 0; padding: 0; box-sizing: border-box; }
  html, body { width: 1200px; height: 900px; overflow: hidden; }
  body {
    background: var(--backdrop);
    position: relative;
    font-family: "Open Sans", Arial, sans-serif;
  }
  .card {
    position: absolute;
    top: 300px;
    width: 525px;
    height: 300px;
    background: var(--card-black);
    box-shadow: 0 14px 30px rgba(0,0,0,0.45);
  }
  .card--front { left: 50px; }
  .card--back { left: 625px; display: flex; flex-direction: column; align-items: center; justify-content: center; }

  .brand-block {
    position: absolute;
    left: 24px; top: 0; width: 170px; height: 300px;
    display: flex; flex-direction: column; align-items: center; justify-content: center; gap: 12px;
  }
  .brand-dot {
    width: 54px; height: 54px; border-radius: 50%;
    background: var(--gold);
  }
  .brand-name {
    font-family: "Cinzel", "Times New Roman", serif;
    font-weight: 600;
    color: var(--silver);
    font-size: 15px;
    line-height: 1.3;
    text-align: center;
    letter-spacing: 0.5px;
  }
  .divider {
    position: absolute;
    left: 212px; top: 82px;
    width: 1px; height: 136px;
    background: linear-gradient(to bottom, transparent, var(--rule-gold), transparent);
  }
  .contact-block {
    position: absolute;
    left: 232px; top: 84px;
    color: var(--white);
  }
  .person-name { color: var(--gold); font-weight: 700; font-size: 17px; line-height: 1.2; }
  .person-title { font-size: 12.5px; margin-bottom: 14px; }
  .contact-list { list-style: none; font-size: 12.5px; line-height: 1.55; }
  .contact-list li { display: flex; align-items: center; gap: 10px; }
  .contact-list svg { width: 11px; height: 11px; flex: none; }

  .back-name {
    font-family: "Cinzel", "Times New Roman", serif;
    font-weight: 600;
    color: var(--silver);
    font-size: 26px;
    letter-spacing: 1px;
    text-align: center;
  }
  .back-rule {
    margin-top: 10px;
    width: 230px; height: 1px;
    background: var(--silver);
    opacity: 0.7;
  }
</style>
</head>
<body>
  <section class="card card--front" aria-label="Business card front">
    <div class="brand-block">
      <div class="brand-dot"></div>
      <div class="brand-name">Harbor &amp; Summit<br>Gatherings</div>
    </div>
    <div class="divider"></div>
    <div class="contact-block">
      <p class="person-name">Darcy Whitlow</p>
      <p class="person-title">Event and Conference Specialist</p>
      <ul class="contact-list">
        <li>
          <svg viewBox="0 0 12 12" aria-hidden="true"><rect x="3" y="0.5" width="6" height="11" rx="1" fill="none" stroke="#d9ad2e" stroke-width="1.2"/><circle cx="6" cy="9.5" r="0.8" fill="#d9ad2e"/></svg>
          +61 (0) 491 338 027
        </li>
        <li>
          <svg viewBox="0 0 12 12" aria-hidden="true"><path d="M2 1.5 L4.5 1 L5.5 3.8 L4 5 Q5 7 7 8 L8.2 6.5 L11 7.5 L10.5 10 Q5 10.5 1.5 3 Z" fill="#d9ad2e"/></svg>
          1300 862 419
        </li>
        <li>
          <svg viewBox="0 0 12 12" aria-hidden="true"><rect x="0.5" y="2" width="11" height="8" fill="#d9ad2e"/><path d="M0.5 2 L6 6.5 L11.5 2" fill="none" stroke="#0c0c0c" stroke-width="1"/></svg>
          darcyw@harborandsummit.com.au
        </li>
        <li>
          <svg viewBox="0 0 12 12" aria-hidden="true"><circle cx="6" cy="6" r="5.3" fill="none" stroke="#d9ad2e" stroke-width="1.2"/><ellipse cx="6" cy="6" rx="2.3" ry="5.3" fill="none" stroke="#d9ad2e" stroke-width="1"/><line x1="0.7" y1="6" x2="11.3" y2="6" stroke="#d9ad2e" stroke-width="1"/></svg>
          www.harborandsummit.com.au
        </li>
      </ul>
    </div>
  </section>

  <section class="card card--back" aria-label="Business card back">
    <p class="back-name">Harbor &amp; Summit<br>Gatherings</p>
    <div class="back-rule"></div>
  </section>
</body>
</html>
```